Holloway Kin Playing Cards

We are wanting a cool design for a playing card that includes our logo(s). I will attach our two logos, we are open to using either one of them or another version of them. I will also attach some pictures of card decks to use for inspiration. These are just decks that we have seen from other artists that we liked. We are located in West Texas so although not necessary, a Sotol or Agave or cactus or quail (bird) or some sort of sunset would pay homage to our surroundings. I realize the examples are all very different, but those are just some decks that we like! Thank you!

```html
<!DOCTYPE html>
<html lang="en">
<head>
<meta charset="utf-8">
<title>Holloway Kin Playing Cards – Tuck Box Front</title>
<link rel="stylesheet" href="https://fonts.googleapis.com/css2?family=Passion+One:wght@700&family=Montserrat:wght@700&display=swap">
<style>
  :root {
    --page-bg: #eef0f3;
    --box-blue: #1c4c96;
    --box-blue-deep: #153c7c;
    --navy: #0b1e3f;
    --ink-dark: #1b1733;
    --line-white: #ffffff;
    --sky-top: #1d4a93;
    --sky-glow: #f4e7b8;
    --sun-orange: #ef8f2c;
    --sun-yellow: #f3c63e;
    --hill-purple: #4a3f9a;
    --hill-blue: #4f6cc0;
    --text-white: #ffffff;
  }
  * { margin: 0; padding: 0; box-sizing: border-box; }
  html, body {
    width: 1200px; height: 960px; overflow: hidden;
    background: var(--page-bg);
  }
  .canvas {
    position: relative; width: 1200px; height: 960px;
    display: flex; align-items: center; justify-content: center;
  }
  .box-front {
    position: relative; width: 580px; height: 820px;
    background: radial-gradient(circle at 30% 20%, var(--box-blue), var(--box-blue-deep));
    overflow: hidden;
  }
  .thumb-notch {
    position: absolute; top: -62px; left: 50%;
    width: 124px; height: 124px; margin-left: -62px;
    border-radius: 50%; background: var(--box-blue-deep);
    box-shadow: inset 0 -3px 6px rgba(0,0,0,0.25);
    z-index: 3;
  }
  .frame-outer {
    position: absolute; inset: 24px;
    border: 2px solid var(--line-white);
  }
  .frame-inner {
    position: absolute; inset: 34px;
    border: 1.5px solid var(--line-white);
  }
  .scene-panel {
    position: absolute; left: 44px; right: 44px; top: 44px; bottom: 44px;
    overflow: hidden;
    background:
      linear-gradient(to top, var(--ink-dark) 0%, var(--ink-dark) 22%, transparent 22.2%),
      linear-gradient(to top, var(--hill-purple) 0%, var(--hill-purple) 32%, transparent 32.2%),
      linear-gradient(to top, var(--hill-blue) 0%, var(--hill-blue) 38%, transparent 38.2%),
      linear-gradient(to top, var(--sun-yellow) 0%, var(--sun-yellow) 44%, transparent 44.2%),
      linear-gradient(to top, var(--sun-orange) 0%, var(--sun-orange) 52%, transparent 60%),
      linear-gradient(to bottom, var(--sky-top) 0%, #3d63a6 22%, var(--sky-glow) 52%, var(--sky-glow) 100%);
  }
  .brand-mark {
    position: absolute; top: 120px; left: 0; right: 0;
    display: flex; align-items: center; justify-content: center; gap: 14px;
    z-index: 2;
  }
  .brand-dot {
    width: 22px; height: 22px; border-radius: 50%;
    background: var(--text-white);
  }
  .brand-name {
    font-family: "Montserrat", sans-serif; font-weight: 700;
    font-size: 38px; letter-spacing: 4px;
    color: var(--text-white);
  }
  .title-block {
    position: absolute; left: 70px; right: 70px; bottom: 80px; z-index: 2;
    color: var(--text-white);
  }
  .title {
    font-family: "Passion One", sans-serif; font-weight: 700;
    font-size: 62px; line-height: 0.95; letter-spacing: 1px;
    text-transform: uppercase; white-space: nowrap;
  }
  .tagline {
    display: flex; align-items: center; gap: 12px; margin-top: 10px;
    font-family: "Montserrat", sans-serif; font-weight: 700;
    font-size: 16px; letter-spacing: 4px; text-transform: uppercase;
    white-space: nowrap;
  }
  .tagline-rule {
    width: 36px; height: 2px; background: var(--text-white);
  }
</style>
</head>
<body>
  <main class="canvas">
    <section class="box-front">
      <div class="thumb-notch"></div>
      <div class="frame-outer"></div>
      <div class="frame-inner"></div>
      <div class="scene-panel" role="img" aria-label="Illustrated West Texas desert at sunset: starry night sky fading into a glowing horizon, orange mesas, purple hills and dark saguaro and prickly pear cactus silhouettes in the foreground"></div>
      <div class="brand-mark">
        <span class="brand-dot"></span>
        <span class="brand-name">HOLLOWAY KIN</span>
      </div>
      <div class="title-block">
        <h1 class="title">Playing Cards</h1>
        <p class="tagline"><span class="tagline-rule"></span>Forged in West Texas<span class="tagline-rule"></span></p>
      </div>
    </section>
  </main>
</body>
</html>
```